Financial Planning Firm needs a client data collection summary sheet to print on A3

We are a financial advice company, and we are after a 1-page sheet where we can write all of the client’s personal information in our meetings, like a mind map.
It should have our logo on the page along with a place to put the Client's Name and the Date.
It also needs to have the following Headings
Family
Home
Investments
Business
Estate Plan
Lifestyle
Money
Retirement
Dreams & Goals
Health and Wellbeing
It also needs to have our License details on the bottom: Kestrel Counsel Pty Ltd (813962) is an Authorised Representative of Thornbury Capital Partners Pty Ltd AFSL No: 679158 ABN 73 518 926 084. This document has been prepared by Kestrel Counsel and is for general information only.
Please utilise our colour scheme as per our logo attached. Please find uploaded to the project an example data collection summary sheet that we use currently.

```html
<!DOCTYPE html>
<html lang="en">
<head>
<meta charset="utf-8">
<title>Kestrel Counsel – Client Summary Sheet</title>
<link href="https://fonts.googleapis.com/css2?family=Arimo&family=Bebas+Neue&display=swap" rel="stylesheet">
<style>
  :root {
    --stage: #ebebeb;
    --gold: #c9a06a;
    --ink: #000000;
    --paper: #ffffff;
    --legal-dark: #6e5737;
    --legal-light: #4a4a4a;
  }
  * { box-sizing: border-box; margin: 0; padding: 0; }
  html, body {
    width: 1200px; height: 1200px; overflow: hidden;
    background: var(--stage);
  }
  .stage { position: relative; width: 1200px; height: 1200px; }

  .sheet {
    position: absolute; width: 700px; height: 495px;
    font-family: "Bebas Neue", "Oswald", sans-serif;
  }
  .sheet--dark  { left: 247px; top: 53px;  background: var(--ink);   --disc: var(--gold); --brand: var(--paper); --legal: var(--legal-dark); }
  .sheet--light { left: 250px; top: 645px; background: var(--paper); --disc: var(--ink);  --brand: var(--ink);   --legal: var(--legal-light); }

  .field { position: absolute; top: 45px; color: var(--gold); font-size: 7px; letter-spacing: .3px; border-bottom: 1px solid var(--gold); height: 10px; }
  .field--name { left: 33px; width: 237px; }
  .field--date { left: 335px; width: 110px; }

  .brand {
    position: absolute; left: 512px; top: 24px; width: 146px;
    text-align: center; color: var(--brand);
    font-size: 17px; letter-spacing: 2.6px; line-height: 1;
  }

  .topic {
    position: absolute; width: 130px; margin-left: -65px;
    text-align: center; color: var(--gold);
  }
  .topic svg { display: block; width: 40px; height: 40px; margin: 0 auto; }
  .topic .disc { fill: var(--disc); }
  .topic .glyph { fill: none; stroke: var(--paper); stroke-width: .9; stroke-linecap: round; stroke-linejoin: round; }
  .topic__label { display: block; margin-top: 9px; font-size: 17px; letter-spacing: .4px; line-height: 1; }
  .row-1 { top: 124px; }
  .row-2 { top: 300px; }
  .col-1 { left: 86px; } .col-2 { left: 218px; } .col-3 { left: 349px; } .col-4 { left: 480px; } .col-5 { left: 612px; }

  .legal {
    position: absolute; left: 0; right: 0; top: 448px;
    text-align: center; color: var(--legal);
    font-family: "Arimo", Arial, sans-serif;
  }
  .legal__licence { font-size: 7.6px; line-height: 8.6px; }
  .legal__notice { font-size: 6px; margin-top: 8px; }
</style>
</head>
<body>
<svg width="0" height="0" style="position:absolute" aria-hidden="true">
  <defs>
    <symbol id="i-heart" viewBox="0 0 40 40"><path d="M20 30 C10 22 8 18 8 15 a6 6 0 0 1 12 -1 a6 6 0 0 1 12 1 c0 3 -2 7 -12 15z"/></symbol>
    <symbol id="i-home" viewBox="0 0 40 40"><path d="M6 20 L20 9 L34 20 M10 18 V31 H30 V18 M13 31 V24 H18 V31 M21 23 H27 V27 H21 Z M27 13 V10 H30 V15 M5 32 H35"/></symbol>
    <symbol id="i-coins" viewBox="0 0 40 40"><circle cx="20" cy="14" r="5"/><circle cx="13" cy="24" r="5"/><circle cx="27" cy="24" r="5"/><path d="M20 11 V17 M18.5 12.5 h3 M18.5 15.5 h3 M12 22 v5 h3 M11 24.5 h3 M25.5 22 l1.5 2 l1.5 -2 M27 24 v3 M25.5 25 h3"/></symbol>
    <symbol id="i-globe" viewBox="0 0 40 40"><circle cx="20" cy="20" r="11"/><ellipse cx="20" cy="20" rx="5" ry="11"/><path d="M9 20 H31 M11 14 H29 M11 26 H29 M20 9 V31"/></symbol>
    <symbol id="i-doc" viewBox="0 0 40 40"><path d="M14 9 H26 V31 H14 Z M16 13 H24 M16 15.5 H24 M16 18 H24 M16 20.5 H22 M21 28 H24"/></symbol>
    <symbol id="i-chair" viewBox="0 0 40 40"><path d="M12 21 V13 Q20 9 28 13 V21 M9 21 H13 V30 H9 Z M27 21 H31 V30 H27 Z M13 25 H27 M13 21 Q20 19 27 21"/></symbol>
    <symbol id="i-stack" viewBox="0 0 40 40"><ellipse cx="17" cy="11" rx="7" ry="2.5"/><path d="M10 11 V25 M24 11 V22 M10 14.5 a7 2.5 0 0 0 14 0 M10 18 a7 2.5 0 0 0 14 0 M10 21.5 a7 2.5 0 0 0 8 2"/><ellipse cx="25" cy="24" rx="7" ry="2.5"/><path d="M18 24 V30 a7 2.5 0 0 0 14 0 V24 M18 27 a7 2.5 0 0 0 14 0"/></symbol>
    <symbol id="i-sun" viewBox="0 0 40 40"><circle cx="20" cy="14" r="3.5"/><path d="M20 7 v2 M20 19 v2 M13 14 h2 M25 14 h2 M15 9 l1.4 1.4 M23.6 17.6 l1.4 1.4 M25 9 l-1.4 1.4 M16.4 17.6 l-1.4 1.4 M6 32 L16 23 L22 28 L26 25 L34 32 Z"/></symbol>
    <symbol id="i-moon" viewBox="0 0 40 40"><path d="M24 9 A11 11 0 1 0 31 27 A9 9 0 1 1 24 9 Z"/><path d="M25 12 l1.3 2.7 3 .4 -2.2 2 .6 3 -2.7 -1.5 -2.7 1.5 .6 -3 -2.2 -2 3 -.4 Z"/></symbol>
    <symbol id="i-scope" viewBox="0 0 40 40"><path d="M17 9 V11 M27 9 V11 M17 11 Q14 12 14 18 Q14 25 22 25 Q30 25 30 18 Q30 12 27 11 M22 25 V29 Q22 32 18 32 Q14 32 14 29 V27"/><circle cx="13" cy="24" r="2.3"/></symbol>
  </defs>
</svg>

<main class="stage">
  <!-- Dark edition -->
  <section class="sheet sheet--dark">
    <div class="field field--name">NAME</div>
    <div class="field field--date">DATE</div>
    <div class="brand">KESTREL COUNSEL</div>

    <div class="topic row-1 col-1"><svg><circle class="disc" cx="20" cy="20" r="20"/><use class="glyph" href="#i-heart"/></svg><span class="topic__label">Family</span></div>
    <div class="topic row-1 col-2"><svg><circle class="disc" cx="20" cy="20" r="20"/><use class="glyph" href="#i-home"/></svg><span class="topic__label">Home</span></div>
    <div class="topic row-1 col-3"><svg><circle class="disc" cx="20" cy="20" r="20"/><use class="glyph" href="#i-coins"/></svg><span class="topic__label">Investments</span></div>
    <div class="topic row-1 col-4"><svg><circle class="disc" cx="20" cy="20" r="20"/><use class="glyph" href="#i-globe"/></svg><span class="topic__label">Business</span></div>
    <div class="topic row-1 col-5"><svg><circle class="disc" cx="20" cy="20" r="20"/><use class="glyph" href="#i-doc"/></svg><span class="topic__label">Estate Plan</span></div>
    <div class="topic row-2 col-1"><svg><circle class="disc" cx="20" cy="20" r="20"/><use class="glyph" href="#i-chair"/></svg><span class="topic__label">Lifestyle</span></div>
    <div class="topic row-2 col-2"><svg><circle class="disc" cx="20" cy="20" r="20"/><use class="glyph" href="#i-stack"/></svg><span class="topic__label">Money</span></div>
    <div class="topic row-2 col-3"><svg><circle class="disc" cx="20" cy="20" r="20"/><use class="glyph" href="#i-sun"/></svg><span class="topic__label">Retirement</span></div>
    <div class="topic row-2 col-4"><svg><circle class="disc" cx="20" cy="20" r="20"/><use class="glyph" href="#i-moon"/></svg><span class="topic__label">Dreams &amp; Goals</span></div>
    <div class="topic row-2 col-5"><svg><circle class="disc" cx="20" cy="20" r="20"/><use class="glyph" href="#i-scope"/></svg><span class="topic__label">Health &amp; Wellbeing</span></div>

    <footer class="legal">
      <p class="legal__licence">Kestrel Counsel Pty Ltd (813962) is an Authorised Representative of Thornbury Capital Partners Pty Ltd<br>AFSL No: 679158 ABN 73 518 926 084.</p>
      <p class="legal__notice">This document has been prepared by Kestrel Counsel and is for General Information Only.</p>
    </footer>
  </section>

  <!-- Light edition -->
  <section class="sheet sheet--light">
    <div class="field field--name">NAME</div>
    <div class="field field--date">DATE</div>
    <div class="brand">KESTREL COUNSEL</div>

    <div class="topic row-1 col-1"><svg><circle class="disc" cx="20" cy="20" r="20"/><use class="glyph" href="#i-heart"/></svg><span class="topic__label">Family</span></div>
    <div class="topic row-1 col-2"><svg><circle class="disc" cx="20" cy="20" r="20"/><use class="glyph" href="#i-home"/></svg><span class="topic__label">Home</span></div>
    <div class="topic row-1 col-3"><svg><circle class="disc" cx="20" cy="20" r="20"/><use class="glyph" href="#i-coins"/></svg><span class="topic__label">Investments</span></div>
    <div class="topic row-1 col-4"><svg><circle class="disc" cx="20" cy="20" r="20"/><use class="glyph" href="#i-globe"/></svg><span class="topic__label">Business</span></div>
    <div class="topic row-1 col-5"><svg><circle class="disc" cx="20" cy="20" r="20"/><use class="glyph" href="#i-doc"/></svg><span class="topic__label">Estate Plan</span></div>
    <div class="topic row-2 col-1"><svg><circle class="disc" cx="20" cy="20" r="20"/><use class="glyph" href="#i-chair"/></svg><span class="topic__label">Lifestyle</span></div>
    <div class="topic row-2 col-2"><svg><circle class="disc" cx="20" cy="20" r="20"/><use class="glyph" href="#i-stack"/></svg><span class="topic__label">Money</span></div>
    <div class="topic row-2 col-3"><svg><circle class="disc" cx="20" cy="20" r="20"/><use class="glyph" href="#i-sun"/></svg><span class="topic__label">Retirement</span></div>
    <div class="topic row-2 col-4"><svg><circle class="disc" cx="20" cy="20" r="20"/><use class="glyph" href="#i-moon"/></svg><span class="topic__label">Dreams &amp; Goals</span></div>
    <div class="topic row-2 col-5"><svg><circle class="disc" cx="20" cy="20" r="20"/><use class="glyph" href="#i-scope"/></svg><span class="topic__label">Health &amp; Wellbeing</span></div>

    <footer class="legal">
      <p class="legal__licence">Kestrel Counsel Pty Ltd (813962) is an Authorised Representative of Thornbury Capital Partners Pty Ltd<br>AFSL No: 679158 ABN 73 518 926 084.</p>
      <p class="legal__notice">This document has been prepared by Kestrel Counsel and is for General Information Only.</p>
    </footer>
  </section>
</main>
</body>
</html>
```